Marketing Agency Needs Infographic on Media and People*

We need an infographic that shows how people of multiple generations are “touched” by marketing messages in various ways, every day. As a marketing agency, we need to convey to potential clients that marketing is integrated and all mediums and strategies need to be thoroughly discussed. It needs to easily convey that people are exposed to many messages throughout the day.

*The designer who's infographic we decide on will get a second project from us for another, similar infographic through Brightquill Services*

Font styles to use
Sans Serif

Requirements
Must have
• Clear, easy to see/understand icons and images
Nice to have
• Branded colours - see attached brand guide
Should not have
• Inappropriate images

```html
<!DOCTYPE html>
<html lang="en">
<head>
<meta charset="utf-8">
<title>Generations and Media Touchpoints</title>
<link href="https://fonts.googleapis.com/css2?family=Montserrat:wght@700&display=swap" rel="stylesheet">
<style>
  :root {
    --page: #ffffff;
    --card: #646464;
    --tan: #c9955f;
    --circle: #9b7c62;
    --icon: #a4aaa1;
    --icon-dark: #6f786d;
    --icon-light: #e9ece6;
    --notch: #a6a6a6;
    --ink: #111111;
  }
  html, body {
    margin: 0;
    padding: 0;
    width: 1200px;
    height: 1200px;
    overflow: hidden;
    background: var(--page);
  }
  .infographic {
    position: relative;
    width: 1200px;
    height: 1200px;
  }
  .notch {
    position: absolute;
    width: 46px;
    height: 14px;
    background: var(--notch);
    border-radius: 0 0 14px 14px;
  }
  .generation-card {
    position: absolute;
    width: 272px;
    height: 247px;
    background: var(--card);
    border-radius: 24px;
  }
  .generation-card svg {
    position: absolute;
    inset: 0;
    width: 272px;
    height: 247px;
    overflow: visible;
  }
  .generation-label {
    position: absolute;
    left: 46px;
    top: 231px;
    width: 180px;
    height: 24px;
    border-radius: 12px;
    background: var(--tan);
    color: var(--ink);
    font-family: "Montserrat", sans-serif;
    font-weight: 700;
    font-size: 15px;
    line-height: 24px;
    text-align: center;
  }
  .card-silent { left: 16px; top: 593px; }
  .card-boomer { left: 242px; top: 359px; }
  .card-genx { left: 468px; top: 593px; }
  .card-millennial { left: 694px; top: 359px; }
  .card-genz { left: 919px; top: 593px; }
  .flow-path { fill: none; stroke: var(--tan); stroke-width: 1.6; stroke-dasharray: 5 3; }
  .flow-dot { fill: var(--tan); }
  .flow-arrow { fill: var(--tan); }
  .people-circle { fill: var(--circle); stroke: var(--tan); stroke-width: 2; }
  .icon-fill { fill: var(--icon); }
  .icon-dark { fill: var(--icon-dark); }
  .icon-light { fill: var(--icon-light); }
  .icon-stroke { fill: none; stroke: var(--icon); stroke-width: 3; stroke-linecap: round; }
  .wifi-text { font-family: "Montserrat", sans-serif; font-weight: 700; font-size: 12px; fill: var(--icon-dark); }
</style>
</head>
<body>
<div class="infographic">

  <svg width="0" height="0" style="position:absolute">
    <defs>
      <symbol id="envelope" viewBox="0 0 60 68">
        <path class="icon-fill" d="M0 26 L30 0 L60 26 V68 H0 Z"/>
        <rect class="icon-light" x="12" y="18" width="36" height="24"/>
        <rect class="icon-dark" x="16" y="23" width="28" height="2"/>
        <rect class="icon-dark" x="16" y="29" width="28" height="2"/>
        <rect class="icon-dark" x="16" y="35" width="28" height="2"/>
        <path class="icon-fill" d="M0 30 L30 52 L60 30 V68 H0 Z" style="filter:brightness(0.92)"/>
        <circle class="icon-dark" cx="30" cy="48" r="8"/>
        <text x="30" y="52" text-anchor="middle" font-family="Montserrat, sans-serif" font-weight="700" font-size="11" fill="#e9ece6">@</text>
      </symbol>
      <symbol id="bubble" viewBox="0 0 52 46">
        <ellipse class="icon-fill" cx="26" cy="18" rx="26" ry="18"/>
        <path class="icon-fill" d="M8 28 L4 46 L20 33 Z"/>
        <circle class="icon-dark" cx="16" cy="18" r="3.5"/>
        <circle class="icon-dark" cx="26" cy="18" r="3.5"/>
        <circle class="icon-dark" cx="36" cy="18" r="3.5"/>
      </symbol>
      <symbol id="handset" viewBox="0 0 56 56">
        <path class="icon-fill" d="M8 6 L18 2 L24 16 L17 21 C19 29 25 36 32 40 L38 34 L52 41 L48 52 C30 54 6 32 8 6 Z"/>
        <path class="icon-stroke" d="M30 4 A22 22 0 0 1 52 26"/>
        <path class="icon-stroke" d="M30 12 A14 14 0 0 1 44 26"/>
      </symbol>
      <symbol id="document" viewBox="0 0 46 54">
        <rect class="icon-light" x="0" y="4" width="40" height="50"/>
        <rect class="icon-dark" x="5" y="10" width="30" height="3"/>
        <rect class="icon-fill" x="5" y="17" width="22" height="2"/>
        <rect class="icon-fill" x="5" y="22" width="22" height="2"/>
        <rect class="icon-fill" x="5" y="27" width="22" height="2"/>
        <rect class="icon-fill" x="5" y="32" width="22" height="2"/>
        <path class="icon-dark" d="M22 44 L40 2 L46 5 L28 47 L21 50 Z"/>
      </symbol>
      <symbol id="smartphone" viewBox="0 0 44 82">
        <rect class="icon-dark" x="0" y="0" width="44" height="82" rx="6"/>
        <rect class="icon-light" x="4" y="10" width="36" height="56"/>
        <circle fill="none" stroke="#e9ece6" stroke-width="2" cx="22" cy="74" r="3.5"/>
        <ellipse class="icon-fill" cx="22" cy="36" rx="11" ry="8"/>
        <path class="icon-fill" d="M16 41 L14 48 L21 43 Z"/>
      </symbol>
      <symbol id="laptop" viewBox="0 0 80 60">
        <rect class="icon-fill" x="4" y="0" width="72" height="52" rx="2"/>
        <rect class="icon-light" x="8" y="8" width="64" height="40"/>
        <rect class="icon-fill" x="12" y="20" width="16" height="2"/>
        <rect class="icon-fill" x="12" y="25" width="16" height="2"/>
        <rect class="icon-fill" x="12" y="30" width="16" height="2"/>
        <rect class="icon-fill" x="12" y="35" width="16" height="2"/>
        <rect class="icon-dark" x="32" y="24" width="20" height="16"/>
        <rect class="icon-dark" x="56" y="32" width="3" height="8"/>
        <rect class="icon-dark" x="61" y="26" width="3" height="14"/>
        <rect class="icon-dark" x="66" y="30" width="3" height="10"/>
        <rect class="icon-light" x="0" y="52" width="80" height="5" rx="2"/>
      </symbol>
    </defs>
  </svg>

  <div class="notch" style="left:242px; top:593px;"></div>
  <div class="notch" style="left:468px; top:593px;"></div>
  <div class="notch" style="left:694px; top:593px;"></div>
  <div class="notch" style="left:919px; top:593px;"></div>

  <!-- Boomer -->
  <section class="generation-card card-boomer">
    <svg viewBox="0 0 272 247">
      <path class="flow-path" d="M42 238 Q20 160 58 97"/>
      <path class="flow-path" d="M60 238 Q45 170 70 117"/>
      <path class="flow-path" d="M230 238 Q262 150 210 103"/>
      <path class="flow-path" d="M214 238 Q238 200 220 145"/>
      <path class="flow-arrow" d="M62 92 L60 110 L55 102 L47 104 Z"/>
      <path class="flow-arrow" d="M176 95 L193 98 L186 102 L186 111 Z"/>
      <circle class="flow-dot" cx="70" cy="117" r="7"/>
      <circle class="flow-dot" cx="216" cy="94" r="7"/>
      <circle class="flow-dot" cx="219" cy="160" r="7"/>
      <g role="img" aria-label="Address book icon">
        <rect class="icon-fill" x="78" y="37" width="48" height="66" rx="3"/>
        <circle class="icon-light" cx="103" cy="70" r="14"/>
      </g>
      <use href="#envelope" x="145" y="16" width="60" height="68"/>
      <circle class="people-circle" cx="136" cy="188" r="64"/>
      <rect role="img" aria-label="Illustration of a Boomer couple" x="74" y="140" width="124" height="107" fill="var(--circle)" opacity="0"/>
    </svg>
    <div class="generation-label">Boomer</div>
  </section>

  <!-- Millennial -->
  <section class="generation-card card-millennial">
    <svg viewBox="0 0 272 247">
      <path class="flow-path" d="M32 157 Q30 215 60 245"/>
      <path class="flow-path" d="M60 157 Q52 215 80 245"/>
      <path class="flow-path" d="M84 63 Q100 50 118 46"/>
      <path class="flow-path" d="M80 123 Q95 110 104 108"/>
      <path class="flow-path" d="M140 99 Q170 100 186 116"/>
      <path class="flow-path" d="M214 79 Q222 86 226 95"/>
      <path class="flow-path" d="M240 146 Q235 210 200 245"/>
      <path class="flow-path" d="M211 163 Q215 210 195 245"/>
      <circle class="flow-dot" cx="78" cy="61" r="7"/>
      <circle class="flow-dot" cx="80" cy="122" r="7"/>
      <circle class="flow-dot" cx="139" cy="98" r="7"/>
      <circle class="flow-dot" cx="213" cy="79" r="7"/>
      <circle class="flow-dot" cx="211" cy="155" r="7"/>
      <circle class="flow-dot" cx="240" cy="146" r="7"/>
      <use href="#smartphone" x="25" y="71" width="44" height="82"/>
      <rect role="img" aria-label="Satellite dish icon" class="icon-fill" x="92" y="68" width="36" height="48" rx="6"/>
      <use href="#laptop" x="124" y="11" width="80" height="60"/>
      <use href="#bubble" x="194" y="102" width="52" height="46"/>
      <circle class="people-circle" cx="136" cy="190" r="64"/>
      <rect role="img" aria-label="Illustration of a Millennial couple" x="74" y="140" width="124" height="107" opacity="0"/>
    </svg>
    <div class="generation-label">Millennial</div>
  </section>

  <!-- Silent Generation -->
  <section class="generation-card card-silent">
    <svg viewBox="0 0 272 247">
      <path class="flow-path" d="M46 238 Q18 160 54 99"/>
      <path class="flow-path" d="M62 238 Q45 160 78 111"/>
      <path class="flow-path" d="M212 238 Q260 160 194 76"/>
      <path class="flow-path" d="M200 238 Q228 200 219 162"/>
      <path class="flow-path" d="M150 86 Q190 95 212 140"/>
      <path class="flow-arrow" d="M60 92 L58 110 L52 102 L44 104 Z"/>
      <path class="flow-arrow" d="M139 87 L157 82 L152 89 L156 97 Z"/>
      <circle class="flow-dot" cx="78" cy="111" r="7"/>
      <circle class="flow-dot" cx="194" cy="74" r="7"/>
      <circle class="flow-dot" cx="218" cy="162" r="7"/>
      <use href="#handset" x="78" y="60" width="52" height="52"/>
      <use href="#document" x="136" y="19" width="46" height="54"/>
      <circle class="people-circle" cx="136" cy="188" r="64"/>
      <rect role="img" aria-label="Illustration of a Silent Generation couple" x="74" y="140" width="124" height="107" opacity="0"/>
    </svg>
    <div class="generation-label">Silent Generation</div>
  </section>

  <!-- Gen X -->
  <section class="generation-card card-genx">
    <svg viewBox="0 0 272 247">
      <path class="flow-path" d="M46 238 Q18 160 42 112"/>
      <path class="flow-path" d="M62 238 Q45 170 64 133"/>
      <path class="flow-path" d="M228 238 Q258 190 228 118"/>
      <path class="flow-path" d="M212 238 Q235 200 210 130"/>
      <path class="flow-path" d="M128 89 Q155 88 172 96"/>
      <path class="flow-path" d="M173 62 Q183 64 190 70"/>
      <path class="flow-path" d="M113 61 Q116 58 118 60"/>
      <path class="flow-arrow" d="M50 110 L46 128 L41 119 L33 121 Z"/>
      <path class="flow-arrow" d="M202 126 L216 124 L208 130 L206 138 Z"/>
      <circle class="flow-dot" cx="64" cy="132" r="7"/>
      <circle class="flow-dot" cx="104" cy="60" r="7"/>
      <circle class="flow-dot" cx="128" cy="89" r="7"/>
      <circle class="flow-dot" cx="173" cy="62" r="7"/>
      <circle class="flow-dot" cx="227" cy="117" r="7"/>
      <use href="#handset" x="44" y="60" width="56" height="56"/>
      <use href="#envelope" x="117" y="24" width="44" height="50"/>
      <use href="#bubble" x="178" y="74" width="50" height="45"/>
      <circle class="people-circle" cx="136" cy="190" r="64"/>
      <rect role="img" aria-label="Illustration of a Gen X couple in business wear" x="74" y="140" width="124" height="107" opacity="0"/>
    </svg>
    <div class="generation-label">Gen X</div>
  </section>

  <!-- Gen Z -->
  <section class="generation-card card-genz">
    <svg viewBox="0 0 272 247">
      <path class="flow-path" d="M34 111 Q38 92 45 84"/>
      <path class="flow-path" d="M62 117 Q80 90 106 82"/>
      <path class="flow-path" d="M93 38 Q150 20 185 38"/>
      <path class="flow-path" d="M170 88 Q190 95 203 110"/>
      <path class="flow-path" d="M225 157 Q220 210 190 245"/>
      <path class="flow-path" d="M245 110 Q250 190 210 245"/>
      <path class="flow-path" d="M50 200 Q60 230 78 245"/>
      <path class="flow-arrow" d="M245 93 L252 109 L245 105 L238 111 Z"/>
      <path class="flow-arrow" d="M56 183 L68 196 L59 195 L55 202 Z"/>
      <circle class="flow-dot" cx="28" cy="117" r="7"/>
      <circle class="flow-dot" cx="64" cy="120" r="7"/>
      <circle class="flow-dot" cx="93" cy="39" r="7"/>
      <circle class="flow-dot" cx="170" cy="86" r="7"/>
      <circle class="flow-dot" cx="226" cy="163" r="7"/>
      <circle class="flow-dot" cx="39" cy="193" r="7"/>
      <g role="img" aria-label="Microphone icon">
        <rect class="icon-fill" x="43" y="21" width="28" height="46" rx="14"/>
        <rect class="icon-fill" x="55" y="67" width="4" height="12"/>
        <rect class="icon-fill" x="45" y="79" width="24" height="4" rx="2"/>
      </g>
      <g role="img" aria-label="Tablet with touch icon">
        <rect class="icon-dark" x="110" y="38" width="46" height="64" rx="3"/>
        <rect class="icon-light" x="114" y="44" width="38" height="52"/>
      </g>
      <g role="img" aria-label="Headset icon">
        <path class="icon-stroke" d="M183 62 Q183 28 207 28 Q231 28 231 62" style="stroke-width:3"/>
        <rect class="icon-fill" x="177" y="57" width="14" height="24" rx="6"/>
        <rect class="icon-fill" x="224" y="57" width="14" height="24" rx="6"/>
      </g>
      <g>
        <path class="icon-stroke" d="M30 130 Q42 122 54 130" style="stroke-width:2.5"/>
        <path class="icon-stroke" d="M35 136 Q42 131 49 136" style="stroke-width:2.5"/>
        <circle class="icon-fill" cx="42" cy="141" r="2.5"/>
        <rect class="icon-light" x="18" y="146" width="47" height="21"/>
        <text class="wifi-text" x="41.5" y="161" text-anchor="middle">Wi-Fi</text>
      </g>
      <g role="img" aria-label="Chat bubble icon">
        <rect class="icon-light" x="196" y="110" width="42" height="34" rx="4"/>
        <path class="icon-light" d="M208 144 L206 154 L216 144 Z"/>
      </g>
      <circle class="people-circle" cx="136" cy="190" r="64"/>
      <rect role="img" aria-label="Illustration of a Gen Z pair of students" x="74" y="140" width="124" height="107" opacity="0"/>
    </svg>
    <div class="generation-label">Gen Z</div>
  </section>

</div>
</body>
</html>
```